BSC Flyer to attract applicants 11x17

Brightline Stagecraft Company provides crew for local concerts, filming, theater, and corporate events.
The flyer will be posted on bulletin boards at colleges with theater programs.
Our primary venues are historic theaters in downtown LA
Need a 11x17 poster to attract potential applicants/crew
I have attached a poster that one of our staff made that has all if the relevant info - but i know the poster can look much better than that. I have also attached many images and our logo. It is not necessary to use all of the images, or any of them. The two images of the theater interiors are the venues we operate so they would be the first to include. I can send additional info or images upon request. Thank you

Entertainment

• APPLY@BSCCREWHUB.LA

```html
<!DOCTYPE html>
<html lang="en">
<head>
<meta charset="utf-8">
<title>Brightline Stagecraft Company – Open Positions</title>
<link rel="stylesheet" href="https://fonts.googleapis.com/css2?family=Cinzel:wght@700&family=Poppins:ital,wght@0,400;0,600;1,600&display=swap">
<style>
  :root {
    --backdrop: #8d8d8d;
    --navy-deep: #121a4d;
    --navy: #1b2470;
    --violet: #2c2fa0;
    --ring-blue: #2f5fd8;
    --amber: #f5a31c;
    --white: #ffffff;
    --ink: #1a1a1a;
  }
  * { box-sizing: border-box; margin: 0; padding: 0; }
  html, body { width: 1200px; height: 2777px; overflow: hidden; }
  body { background: var(--backdrop); position: relative; font-family: "Poppins", sans-serif; }

  .poster {
    position: absolute; left: 50px; top: 550px; width: 1100px; height: 1676px;
    overflow: hidden;
    background: linear-gradient(180deg, var(--violet) 0%, var(--navy) 45%, var(--navy-deep) 100%);
    box-shadow: 0 20px 40px rgba(0,0,0,.35);
  }
  .backdrop-photo {
    position: absolute; left: 0; top: 0; width: 1100px; height: 620px;
    background: linear-gradient(160deg, #3437b0 0%, #262a8c 45%, rgba(27,36,112,0) 100%);
  }
  .skyline-photo {
    position: absolute; left: 0; top: 1060px; width: 1100px; height: 400px;
    background: linear-gradient(180deg, rgba(27,36,112,0) 0%, #1f3a8f 45%, #16306f 70%, rgba(18,26,77,0) 100%);
  }
  .venue-ring { position: absolute; left: 0; top: 0; }
  .venue-photo {
    position: absolute; left: 632px; top: 430px; width: 560px; height: 560px; border-radius: 50%;
    background: radial-gradient(circle at 40% 35%, #e7d7e8 0%, #b46aa0 18%, #c86a2a 40%, #6a2540 70%, #2a1740 100%);
  }

  .brand { position: absolute; left: 59px; top: 59px; width: 633px; text-align: center; color: var(--white); }
  .brand-dot { width: 200px; height: 200px; border-radius: 50%; border: 22px solid var(--white); margin: 0 auto 40px; }
  .brand-name { font-family: "Cinzel", serif; font-weight: 700; font-size: 40px; line-height: 1; white-space: nowrap; }
  .brand-sub { display: flex; align-items: center; gap: 14px; margin-top: 12px; font-family: "Cinzel", serif; font-weight: 700; font-size: 26px; letter-spacing: 22px; }
  .brand-sub .rule { flex: 1; height: 4px; background: var(--white); }

  .headline { position: absolute; left: 62px; top: 640px; font-family: "Cinzel", serif; font-weight: 700; font-size: 136px; line-height: 140px; letter-spacing: -2px; color: var(--white); }
  .headline .accent { color: var(--amber); }
  .divider { position: absolute; left: 65px; top: 1096px; width: 855px; height: 3px; background: var(--amber); }

  .pitch { position: absolute; left: 60px; top: 1125px; font-size: 43px; line-height: 59px; color: var(--white); white-space: nowrap; }
  .pitch em { color: var(--amber); font-weight: 600; }
  .pitch strong { font-weight: 600; }

  .apply { position: absolute; left: 85px; top: 1364px; width: 646px; height: 66px; border-radius: 33px; background: var(--amber); color: var(--ink); font-size: 30px; display: flex; align-items: center; justify-content: center; }

  .web { position: absolute; left: 80px; top: 1515px; height: 90px; width: 700px; display: flex; align-items: flex-start; }
  .web-arrow-in { flex: none; margin-top: 22px; }
  .web-url { flex: none; margin-left: 55px; margin-top: 20px; font-size: 36px; letter-spacing: 4px; color: var(--white); white-space: nowrap; }
  .web-arrow-out { flex: none; margin-left: 24px; margin-top: 26px; }
</style>
</head>
<body>
  <main class="poster">
    <div class="backdrop-photo" role="img" aria-label="Stage lighting equipment in a dark blue theater rig"></div>
    <div class="skyline-photo" role="img" aria-label="Downtown Los Angeles skyline at night"></div>
    <svg class="venue-ring" width="1100" height="1100" aria-hidden="true">
      <path d="M 640 1000 A 290 290 0 0 1 1100 460" fill="none" stroke="var(--ring-blue)" stroke-width="12"/>
    </svg>
    <div class="venue-photo" role="img" aria-label="Ornate historic theater interior with lit dome and stage"></div>

    <header class="brand">
      <div class="brand-dot"></div>
      <div class="brand-name">BRIGHTLINE STAGECRAFT</div>
      <div class="brand-sub"><span class="rule"></span>COMPANY<span class="rule"></span></div>
    </header>

    <h1 class="headline">HAS<br>OPEN<br><span class="accent">POSITIONS</span></h1>
    <div class="divider"></div>

    <p class="pitch">We are looking for<br>talented <em>TECHNICIANS</em> to add to our<br><strong>Roster of Skilled Professionals</strong></p>

    <div class="apply">Send Resume to: apply@bsccrewhub.la</div>

    <div class="web">
      <svg class="web-arrow-in" width="80" height="40" aria-hidden="true">
        <path d="M4 32 Q 35 14 74 12" fill="none" stroke="var(--white)" stroke-width="3"/>
        <path d="M62 4 L74 12 L63 20" fill="none" stroke="var(--white)" stroke-width="3"/>
      </svg>
      <div class="web-url">www.bsccrewhub.la</div>
      <svg class="web-arrow-out" width="50" height="70" aria-hidden="true">
        <path d="M40 62 Q 28 34 8 10" fill="none" stroke="var(--white)" stroke-width="3"/>
        <path d="M6 24 L8 10 L20 14" fill="none" stroke="var(--white)" stroke-width="3"/>
      </svg>
    </div>
  </main>
</body>
</html>
```